Harbor Sprig small batch hot sauce label project

I am launching a line of small batch sauces (hot sauces, bbq sauces) and I need a label for my bottles. I have a logo that I like, I'm not completely married to it but It is a good logo. I would like the name of my business and the name of the sauce on the label. Something fun, edgy that would make you want to pick it up off the shelf.

Target Market(s)

Milennials, food bloggers, stay at home moms who want to amp up their dishes with a really good sauce

Industry/Entity Type

Cooking

Requirements
Must have
• I am open to interpretation
Nice to have
• Maybe a bomb cloud since I want to go in the sauce bomb direction.

```html
<!DOCTYPE html>
<html lang="en">
<head>
<meta charset="utf-8">
<title>Harbor Sprig Hot Sauce Label</title>
<link rel="stylesheet" href="https://fonts.googleapis.com/css2?family=Libre+Baskerville:wght@700&family=Yellowtail&display=swap">
<style>
  :root {
    --page: #ffffff;
    --label-black: #000000;
    --gold: #f2b21c;
    --white: #ffffff;
    --sauce-red: #e3141b;
    --sauce-deep: #8f0a0e;
    --title-shadow: #c50f16;
  }
  * { margin: 0; padding: 0; box-sizing: border-box; }
  html, body {
    width: 1200px;
    height: 1200px;
    overflow: hidden;
    background: var(--page);
  }
  .canvas {
    width: 1200px;
    height: 1200px;
    display: flex;
    align-items: center;
    justify-content: center;
  }
  .label {
    width: 560px;
    height: 1130px;
    background: var(--label-black);
    border-radius: 44px;
    display: flex;
    flex-direction: column;
    align-items: center;
    padding-top: 60px;
    font-family: "Libre Baskerville", "Times New Roman", serif;
    font-weight: 700;
  }
  .brand {
    display: flex;
    flex-direction: column;
    align-items: center;
    gap: 22px;
  }
  .brand-mark {
    width: 64px;
    height: 64px;
    border: 6px solid var(--gold);
  }
  .brand-name {
    color: var(--gold);
    font-size: 30px;
    letter-spacing: 3px;
    text-transform: uppercase;
  }
  .title-block {
    position: relative;
    margin-top: 30px;
    width: 540px;
    height: 500px;
  }
  .title-splash {
    position: absolute;
    inset: 0;
    width: 540px;
    height: 500px;
  }
  .title-text {
    position: absolute;
    inset: 0;
    display: flex;
    flex-direction: column;
    align-items: center;
    justify-content: center;
    font-family: "Yellowtail", cursive;
    font-weight: 400;
    color: var(--white);
    line-height: 0.85;
    transform: rotate(-12deg);
    text-shadow: 5px 6px 0 var(--title-shadow), 9px 11px 0 var(--sauce-deep);
  }
  .title-hot {
    font-size: 170px;
    margin-left: 70px;
  }
  .title-sauce {
    font-size: 170px;
    margin-right: 30px;
  }
  .flavors {
    margin-top: 60px;
    color: var(--gold);
    font-size: 42px;
    line-height: 1.45;
    text-align: center;
    list-style: none;
  }
  .net-weight {
    margin-top: 36px;
    color: var(--white);
    font-size: 32px;
  }
</style>
</head>
<body>
  <main class="canvas">
    <section class="label">
      <header class="brand">
        <span class="brand-mark"></span>
        <span class="brand-name">Harbor Sprig</span>
      </header>

      <div class="title-block">
        <svg class="title-splash" viewBox="0 0 540 500" role="img" aria-label="Red paint splash ring behind the product title">
          <defs>
            <radialGradient id="splash-fill" cx="50%" cy="50%" r="50%">
              <stop offset="0%" stop-color="#000000"/>
              <stop offset="55%" stop-color="#120001"/>
              <stop offset="68%" stop-color="#e3141b"/>
              <stop offset="90%" stop-color="#8f0a0e"/>
              <stop offset="100%" stop-color="#000000"/>
            </radialGradient>
          </defs>
          <ellipse cx="270" cy="250" rx="262" ry="240" fill="url(#splash-fill)"/>
        </svg>
        <h1 class="title-text">
          <span class="title-hot">Hot</span>
          <span class="title-sauce">Sauce</span>
        </h1>
      </div>

      <ul class="flavors">
        <li>Habanero</li>
        <li>Onion</li>
        <li>Reapers</li>
      </ul>

      <p class="net-weight">NET WT. 5 oz</p>
    </section>
  </main>
</body>
</html>
```